依頼詳細
人生100年時代・老後2000万円問題の解決に関するセミナーを行いたいと思っており、メインターゲット層はシニア(富裕層)で若年層までと考えております。開催日程は追記します。チラシ配布は5回、セミナー開催は10回(各チラシ2日程を載せる)を予定しています。
初めての取り組みであり、全くの素人なのでアドバイスや一歩先のご提案をいただけると助かります。
記載項目
会社ロゴ、電話番号、https://www.komo-ast.jp/、裏面は添付PDFの文章が必要となります。
サイズ
A4
ページ数
両面
希望イメージ
シンプル 複雑
単色 カラフル
暗い 明るい
日常 高級
遊び心 厳粛
未来的 伝統的
女性的 男性的
希望する色
赤系、茶系
納品ファイル
• 高解像度JPG (.jpg)
• イラストレーター形式 (.ai)
• PNG形式 (.png)
補足説明
日程・写真等をこちらで編集したいので、編集できるファイルが欲しいです。
補足事項を追記させていただきます。
翠嶺証券のアドバイザーであることがわかるようにロゴを入れていただき、「関東財務局長(金商)第736号」を入れていただきたいです。
また裏面のIFAの説明、ヒアリングからフォローまでの流れのデザインを変更、
翠嶺証券の住所が「東京都港区北白浜4-3-17」に変更になっておりますので修正をお願い致します。
修正部分を写真でアップロードさせていただきます。
金融商品仲介業者:株式会社こもれびアセット 登録番号:近畿財務局長(金仲)第512号/所属金融商品取引業者:翠嶺証券株式会社/登録番号:関東財務局長(金商)第736号 加入協会:全国債券取扱連盟、一般社団法人 資産期約取扱者連盟、全国物産期約売買連盟、一般社団法人 小口運用資産取扱者連絡会、一般社団法人 全国資産助言者連盟
当社は所属金融商品取引業者の代理権はありません。当社は金融商品仲介業務に関し、お客様から金銭や有価証券を直接お預かりすることはありません。
セミナー参加者の方へ、商品の勧誘を行うことがあります。商品等にご投資いただく場合には所定の手数料や諸経費等をご負担いただく場合があります。
また、各商品等には相場の変動等による損失が生じる恐れがあります。各商品等へのご投資にかかる手数料およびリスクについては、当該商品等の契約締結前交付書面等をよくお読みになり内容について十分にご理解ください。
※個人情報の取り扱いについて、本セミナーは株式会社こもれびアセットにより運営されており、個人情報は弊社で管理いたします。ご記入いただきましたお客様の個人情報は弊社の利用目的の範囲内で利用させていただきます。

デザイン・修正依頼の対応の速さ・正確さ・丁寧さに非常に満足できました。

デザイン力、修正依頼の対応の早さや正確さ、丁寧さに非常に満足できました。
また機会がありましたらその他のものも依頼したいと思っております。
この度はありがとうございました。

```html
<!DOCTYPE html>
<html lang="ja">
<head>
<meta charset="UTF-8">
<title>老後2000万円問題に備える 個別セミナー</title>
<link href="https://fonts.googleapis.com/css2?family=Noto+Sans+JP:wght@400;500;700;900&display=swap" rel="stylesheet">
<style>
:root{
  --teal:#1f9e96;
  --teal-dark:#16736f;
  --teal-pale:#d9f0ec;
  --mint:#eaf6f3;
  --navy:#1f3447;
  --orange:#e8742b;
  --white:#ffffff;
  --ink:#333c44;
  --grey:#8d9aa3;
}
*{margin:0;padding:0;box-sizing:border-box}
html,body{width:849px;height:1200px;overflow:hidden;background:#fff}
body{font-family:"Noto Sans JP",sans-serif;color:var(--ink)}
.flyer{position:relative;width:849px;height:1200px;background:linear-gradient(180deg,var(--mint) 0%,#f4fbf9 55%,#fff 100%);overflow:hidden}

.brand-bar{position:absolute;top:0;right:0;width:430px;height:58px;background:var(--teal-dark);border-bottom-left-radius:30px;display:flex;align-items:center;gap:12px;padding-left:40px}
.brand-bar .mark{width:26px;height:26px;border-radius:50%;background:var(--white)}
.brand-bar .name{color:var(--white);font-weight:700;font-size:22px;letter-spacing:1px}

.kicker{position:absolute;top:56px;left:40px;background:var(--teal-dark);color:#fff;font-weight:700;font-size:20px;padding:4px 18px;transform:skewX(-8deg)}
.kicker span{display:inline-block;transform:skewX(8deg)}
.seminar-title{position:absolute;top:92px;left:40px;color:var(--teal);font-weight:900;font-size:44px;letter-spacing:2px;background:var(--white);padding:0 16px;line-height:58px}

.era-tag{position:absolute;top:166px;left:40px;width:40px;height:170px;background:var(--teal);color:#fff;font-weight:700;font-size:20px;writing-mode:vertical-rl;text-align:center;line-height:40px;letter-spacing:2px}
.headline{position:absolute;top:158px;left:96px;color:var(--navy);font-weight:900;font-size:78px;line-height:96px;letter-spacing:1px}

.art-money{position:absolute;top:60px;right:0;width:330px;height:260px;background:radial-gradient(ellipse at 60% 50%,#9fd7c6 0%,#cfeee4 60%,rgba(234,246,243,0) 100%)}
.art-scene{position:absolute;top:330px;left:120px;width:620px;height:230px;background:linear-gradient(180deg,rgba(217,240,236,0) 0%,#cce9e3 60%,#b8e0d8 100%);border-radius:0 0 40px 40px}
.bubble{position:absolute;top:340px;right:70px;width:150px;height:82px;background:#fff;border:2px solid var(--navy);border-radius:50%;display:flex;align-items:center;justify-content:center;text-align:center;font-weight:700;font-size:14px;color:var(--navy);line-height:1.4}

.lead{position:absolute;top:572px;left:0;width:849px;text-align:center;color:var(--teal);font-weight:900;font-size:38px;letter-spacing:1px}
.lead-text{position:absolute;top:630px;left:0;width:849px;text-align:center;font-size:16px;line-height:28px;font-weight:500}

.info{position:absolute;top:710px;left:30px;width:789px;height:160px;background:#fff;border-radius:6px}
.info-row{position:absolute;left:24px;display:flex;align-items:center;gap:18px}
.label{background:var(--teal);color:#fff;font-weight:700;font-size:16px;width:64px;height:34px;display:flex;align-items:center;justify-content:center;letter-spacing:4px}
.row-date{top:16px}
.row-venue{top:66px}
.row-cap{top:118px}
.date{font-weight:900;font-size:34px;color:var(--navy)}
.date small{font-size:22px}
.time{font-size:13px;font-weight:500;line-height:16px}
.venue{font-weight:900;font-size:28px;color:var(--navy);line-height:30px}
.venue small{display:block;font-size:11px;font-weight:500;color:var(--ink);line-height:14px}
.cap{font-weight:700;font-size:20px;color:var(--navy)}
.info .divider{position:absolute;left:24px;right:260px;height:1px;background:var(--teal-pale)}

.apply{position:absolute;top:760px;left:560px;width:82px;height:82px;border-radius:50%;background:var(--teal);color:#fff;font-weight:900;font-size:17px;writing-mode:vertical-rl;display:flex;align-items:center;justify-content:center;line-height:20px}
.free{position:absolute;top:730px;left:660px;width:140px;height:120px;border:3px solid var(--orange);color:var(--orange);font-weight:900;font-size:30px;line-height:40px;display:flex;align-items:center;justify-content:center;text-align:center;background:#fff}

.profiles{position:absolute;top:888px;left:30px;width:789px;display:flex;gap:20px}
.profile{flex:1;display:flex;gap:12px;background:#fff;padding:10px;height:120px}
.photo{width:110px;height:100px;background:linear-gradient(135deg,#c9d3d8,#a9b7bf);display:flex;align-items:center;justify-content:center;color:#fff;font-weight:700;font-size:16px}
.profile h3{font-size:13px;font-weight:700;color:var(--orange);margin-bottom:4px}
.profile p{font-size:10px;line-height:16px;color:var(--ink)}

.footer-note{position:absolute;top:1030px;left:30px;width:789px;font-size:9px;line-height:14px;color:var(--grey)}

.apply-bar{position:absolute;bottom:20px;left:30px;width:789px;height:40px;background:var(--teal-pale);display:flex;align-items:center;gap:16px}
.apply-bar .tag{background:var(--teal-dark);color:#fff;height:100%;display:flex;align-items:center;padding:0 16px;font-weight:700;font-size:15px}
.apply-bar .msg{font-weight:700;font-size:20px;color:var(--navy)}
</style>
</head>
<body>
<div class="flyer">
  <div class="brand-bar"><span class="mark"></span><span class="name">株式会社こもれびアセット</span></div>
  <div class="art-money" role="img" aria-label="積み上げられた紙幣の束のイラスト"></div>

  <div class="kicker"><span>翠嶺証券アドバイザーによる</span></div>
  <div class="seminar-title">個別セミナー開催</div>

  <div class="era-tag">人生100年時代</div>
  <h1 class="headline">老後2000万円<br>問題に備える</h1>

  <div class="art-scene" role="img" aria-label="家と相談する男女のイラスト"></div>
  <div class="bubble">あなたは大丈夫!?<br>みんなやってる!?</div>

  <p class="lead">資産運用のプロから学べるチャンスです。</p>
  <p class="lead-text">独立系ファイナンシャル・アドバイザー(IFA)が資産運用から保険まで<br>お金の悩みを、ぜんぶ解決します！ 明日から実践できる取り組みを教えます。</p>

  <section class="info">
    <div class="info-row row-date"><span class="label">日時</span><span class="date">10月25日<small>(金)</small></span><span class="time">15:00〜17:00<br>(受付開始14:30)</span></div>
    <div class="divider" style="top:58px"></div>
    <div class="info-row row-venue"><span class="label">会場</span><span class="venue">株式会社こもれびアセット<small>和歌山県海南市青葉台318-2-2F</small></span></div>
    <div class="divider" style="top:110px"></div>
    <div class="info-row row-cap"><span class="label">定員</span><span class="cap">先着3名様</span><span class="label">参加費</span><span class="cap">無料</span></div>
  </section>
  <div class="apply">要申込み</div>
  <div class="free">参加費<br>無料!!</div>

  <section class="profiles">
    <div class="profile">
      <div class="photo" role="img" aria-label="講師の写真">写真</div>
      <div><h3>講師：森田 湧一郎さん</h3><p>講師の経歴や実績がここに入ります。資産運用の相談実績多数、わかりやすい解説に定評があります。</p></div>
    </div>
    <div class="profile">
      <div class="photo" role="img" aria-label="会場の写真">写真</div>
      <div><h3>会場：コロナ対策済み</h3><p>会場の案内文がここに入ります。換気と消毒を徹底し、少人数で安心してご参加いただけます。</p></div>
    </div>
  </section>

  <p class="footer-note">金融商品仲介業者：株式会社こもれびアセット 登録番号：近畿財務局長(金仲)第512号／所属金融商品取引業者：翠嶺証券株式会社 登録番号：関東財務局長(金商)第736号</p>

  <div class="apply-bar"><span class="tag">お申込み</span><span class="msg">裏面に詳細説明・セミナー申込書があります。</span></div>
</div>
</body>
</html>
```